Business Card Design Project (Beer industry)

I am seeking a redesign of my business card. I am looking for something that will really stand out in both texture and feel. Something more on the modern side then traditional. Nothing die cut shaped like a beer mug please.

The card is used mostly for other industry professionals, as well as bar and restaurant owners. My title is Strategy & Acquisitions. If you would like to somehow incorporate that theme, that may work.

My business is craft and imported beer. Nothing fizzy and yellow, so my products are more on the upscale side.
Updates

I was able to update my logo in .ai and .tif format. I hope that helps. 

Thank you all for your creative ideas. I have uploaded my current business card in pdf format, as well as our logo in .eps file format. We are excited about the submissions so far and want to thank you all again.

PS Please do not include fax number in future submissions, as we are looking for something more creative and a fax says 1999 and not 2015, which is the message we are going for, without being futuristic. 

Thank you all once again for all of your submissions. If we would consider a two sided card, we would like the opposite side not to be the same as the front. The styles we have seen so far, it appears the front and back are too similar. Again, a two sided card is not required. Thank you and we look forward to pushing the boundaries of your creativity. Cheers

Target Market(s)

My card would mostly go to bar and restaurant operators as well as other beer industry professionals

Industry/Entity Type

Restaurant

Requirements
Nice to have
• Two sided would be considered, although not required
Should not have
• Anything die cut shaped like a beer mug.

```html
<!DOCTYPE html>
<html lang="en">
<head>
<meta charset="utf-8">
<title>Harbor Tap Co. — Business Card</title>
<link rel="stylesheet" href="https://fonts.googleapis.com/css2?family=Rokkitt:wght@800&family=Arimo:wght@400;700&family=Alegreya:ital,wght@1,400;1,700&display=swap">
<style>
  :root {
    --backdrop: #303030;
    --paper: #ffffff;
    --ink: #1f1f1f;
    --band-blue: #3a7ab5;
    --navy: #1d3c66;
    --amber-light: #f0a02a;
    --amber-dark: #d4721a;
    --white: #ffffff;
  }
  * { margin: 0; padding: 0; box-sizing: border-box; }
  html, body {
    width: 1000px; height: 1200px; overflow: hidden;
    background: var(--backdrop);
    font-family: "Arimo", Arial, sans-serif;
  }
  .canvas { position: relative; width: 1000px; height: 1200px; }

  .card { position: absolute; left: 44px; width: 917px; height: 530px; overflow: hidden; }

  /* Front */
  .card-front { top: 21px; background: var(--paper); }
  .front-brand {
    position: absolute; left: 100px; top: 174px;
    display: flex; align-items: center; gap: 12px;
    font-weight: 700; font-size: 30px; color: var(--navy); white-space: nowrap;
  }
  .brand-square { width: 22px; height: 22px; background: var(--navy); flex: none; }
  .holder { position: absolute; right: 47px; top: 68px; text-align: right; }
  .holder-name {
    font-family: "Rokkitt", Georgia, serif; font-weight: 800;
    font-size: 60px; letter-spacing: 4px; color: var(--ink); line-height: 1;
  }
  .holder-title { font-size: 19px; color: var(--ink); margin-top: 2px; }
  .contacts { position: absolute; left: 456px; top: 196px; list-style: none; }
  .contacts li { display: flex; align-items: center; height: 56px; margin-bottom: 14px; }
  .contact-label {
    width: 96px; font-family: "Alegreya", Georgia, serif; font-style: italic; font-weight: 700;
    font-size: 20px; letter-spacing: 1px; color: var(--ink);
    transform: rotate(-14deg); text-align: center;
  }
  .contact-value { font-size: 23px; color: var(--ink); }
  .info-band {
    position: absolute; left: 0; bottom: 0; width: 100%; height: 87px;
    background: var(--band-blue); color: var(--white);
    display: flex; align-items: center; justify-content: center; gap: 26px;
    font-size: 24px; letter-spacing: 0.3px;
  }

  /* Back */
  .card-back {
    top: 643px;
    background: radial-gradient(ellipse at 50% 45%, var(--amber-light) 0%, var(--amber-light) 30%, var(--amber-dark) 100%);
  }
  .back-brand {
    position: absolute; left: 0; right: 0; top: 200px;
    display: flex; align-items: center; justify-content: center; gap: 18px;
    font-weight: 700; font-size: 58px; color: var(--navy);
  }
  .back-brand .brand-square { width: 40px; height: 40px; }
  .back-city {
    position: absolute; left: 0; right: 0; top: 336px; text-align: center;
    font-family: "Alegreya", Georgia, serif; font-style: italic;
    font-size: 42px; color: var(--navy); line-height: 1;
  }
  .tagline {
    position: absolute; left: 0; right: 0; top: 390px; text-align: center;
    font-family: "Alegreya", Georgia, serif; font-style: italic;
    font-size: 20px; color: var(--navy);
  }
</style>
</head>
<body>
<main class="canvas">
  <section class="card card-front" aria-label="Card front">
    <div class="front-brand"><span class="brand-square"></span>Harbor Tap Co.</div>

    <header class="holder">
      <h1 class="holder-name">DALE ORVICK</h1>
      <p class="holder-title">Strategy &amp; Acquisitions</p>
    </header>

    <ul class="contacts">
      <li><span class="contact-label">CELL</span><span class="contact-value">(555) 301-2846</span></li>
      <li><span class="contact-label">EMAIL</span><span class="contact-value">dorvick@mail.com</span></li>
    </ul>

    <footer class="info-band">
      <span class="address">42 Wharf Street Brooklyn, NY 11200</span>
      <span class="website">www.harbortapco.com</span>
    </footer>
  </section>

  <section class="card card-back" aria-label="Card back">
    <div class="back-brand"><span class="brand-square"></span>Harbor Tap Co.</div>
    <p class="back-city">New York</p>
    <p class="tagline">Premier Craft &amp; Import Beer Distributor</p>
  </section>
</main>
</body>
</html>
```